we can communicate on this, but i want to follow the approach we took on Pell|Quorn & Tillet but i feel the card front needs the black background and the platinum and gold logo. The back? I am open. we can use the same info from PQ&T. Vellum Crest is an enhanced equity investment fund - basically a very exclusive boutique hedge fund that uses only stock options. very advanced things. hope you are interested

Contact Information for Business Card

Dr. Owen T. Brisket, CFA
Scientifique de fusée financière
555.014.2296
TheDoc4793@mailvessel.example

4718 Fennel Brook Way N.
Brindle Falls, ND 58999

No web site

Colors

Designer to choose colors to be used in the design.

Requirements
Nice to have
• I tend to prefer the most visible applications of the logo to include logo and name, the logo version with a black background and the gold and platinum components separated by the black. I see this working well for a single side (logo and name - this is card front to me).
• I am fairly open to other treatments on the reverse side with the data. To me, it makes sense to have a different color rendition of the logo on the reverse and it may be a muted black tone on tone or an oversized portion that would have spot UV. Or, the reverse may play with colors and layout
Should not have
• Other colors = no no
• Decorative font

```html
<!DOCTYPE html>
<html lang="en">
<head>
<meta charset="utf-8">
<title>Vellum Crest — Business Card</title>
<link rel="stylesheet" href="https://fonts.googleapis.com/css2?family=Montserrat:wght@400;500;700&display=swap">
<style>
  :root {
    --backdrop: #2a2b2e;
    --card: #1d1e20;
    --card-deep: #0c0c0d;
    --ink-white: #f2f2f2;
    --ink-muted: #d8d8d8;
    --tone-on-tone: #121213;
    --gold: #d9b44a;
    --gold-light: #ecd17a;
    --gold-dark: #b8912c;
    --platinum: #c9c9cc;
  }
  * { box-sizing: border-box; margin: 0; padding: 0; }
  html, body {
    width: 1200px; height: 800px; overflow: hidden;
    background: var(--backdrop);
    font-family: "Montserrat", Arial, sans-serif;
  }
  .canvas { position: relative; width: 1200px; height: 800px; }
  .card {
    position: absolute; width: 600px; height: 343px;
    background: var(--card); overflow: hidden;
    box-shadow: 0 18px 40px rgba(0,0,0,.45);
  }
  /* Front */
  .card-front { left: 140px; top: 34px; }
  .front-decoration {
    position: absolute; left: -120px; top: 40px;
    width: 420px; height: 420px; border-radius: 50%;
    background: radial-gradient(circle at 60% 40%, #151516 0%, var(--card-deep) 70%);
  }
  .front-brand {
    position: absolute; left: 310px; top: 105px; width: 270px;
    display: flex; flex-direction: column; align-items: center; gap: 18px;
    text-align: center;
  }
  .brand-dot {
    width: 70px; height: 70px; border-radius: 50%;
    background: linear-gradient(135deg, var(--platinum) 0%, var(--platinum) 45%, var(--gold) 55%, var(--gold-dark) 100%);
  }
  .front-name {
    font-weight: 700; font-size: 26px; letter-spacing: 2px; white-space: nowrap;
    text-transform: uppercase; color: var(--ink-white);
  }
  /* Back */
  .card-back { left: 460px; top: 423px; }
  .back-brand {
    position: absolute; left: 30px; top: 100px; width: 270px;
    display: flex; flex-direction: column; align-items: center; gap: 16px;
  }
  .back-brand .brand-dot {
    width: 78px; height: 78px;
    background: var(--tone-on-tone);
  }
  .back-name {
    font-weight: 700; font-size: 24px; letter-spacing: 2px; white-space: nowrap;
    text-transform: uppercase; color: var(--tone-on-tone);
  }
  .divider {
    position: absolute; left: 320px; top: 60px; width: 1px; height: 150px;
    background: linear-gradient(to bottom, transparent, var(--gold) 30%, var(--gold) 70%, transparent);
  }
  .contact { position: absolute; left: 345px; top: 78px; }
  .person-name { font-weight: 700; font-size: 16px; color: var(--ink-white); }
  .person-title { font-weight: 500; font-size: 12px; color: var(--gold); margin-top: 4px; }
  .contact-list { list-style: none; margin-top: 22px; }
  .contact-list li {
    display: flex; align-items: center; gap: 8px;
    font-size: 11px; color: var(--ink-muted); margin-bottom: 7px;
  }
  .contact-list svg { flex: none; }
  .address-band {
    position: absolute; left: 0; bottom: 0; width: 100%; height: 52px;
    background: linear-gradient(90deg, var(--gold-dark), var(--gold-light) 50%, var(--gold));
    display: flex; align-items: center; justify-content: center;
    font-weight: 500; font-size: 14px; color: var(--card-deep); letter-spacing: .3px;
  }
</style>
</head>
<body>
<main class="canvas">
  <section class="card card-front" aria-label="Card front">
    <div class="front-decoration" role="img" aria-label="Oversized tone-on-tone brand decoration"></div>
    <div class="front-brand">
      <span class="brand-dot"></span>
      <span class="front-name">Vellum Crest</span>
    </div>
  </section>

  <section class="card card-back" aria-label="Card back">
    <div class="back-brand">
      <span class="brand-dot"></span>
      <span class="back-name">Vellum Crest</span>
    </div>
    <span class="divider"></span>
    <div class="contact">
      <p class="person-name">Dr. Owen T. Brisket, CFA</p>
      <p class="person-title">Scientifique de fusée financière</p>
      <ul class="contact-list">
        <li>
          <svg width="14" height="14" viewBox="0 0 14 14" aria-hidden="true">
            <circle cx="7" cy="7" r="6.3" fill="none" stroke="#d9b44a" stroke-width="1.2"/>
            <path d="M4.6 4.2l1.2-.4.8 1.6-.7.6c.4.8 1 1.4 1.8 1.8l.6-.7 1.6.8-.4 1.2c-2.6 0-4.9-2.3-4.9-4.9z" fill="#d9b44a"/>
          </svg>
          555.014.2296
        </li>
        <li>
          <svg width="14" height="14" viewBox="0 0 14 14" aria-hidden="true">
            <circle cx="7" cy="7" r="6.3" fill="none" stroke="#d9b44a" stroke-width="1.2"/>
            <rect x="4" y="5" width="6" height="4.2" fill="none" stroke="#d9b44a" stroke-width="1"/>
            <path d="M4 5l3 2.3L10 5" fill="none" stroke="#d9b44a" stroke-width="1"/>
          </svg>
          TheDoc4793@mailvessel.example
        </li>
      </ul>
    </div>
    <div class="address-band">4718 Fennel Brook Way N., Brindle Falls, ND 58999</div>
  </section>
</main>
</body>
</html>
```